Carpet cleaning company wants business card

Need an exciting new fresh design for business cards for my carpet cleaning /pest control business
www.tidewellhomecare.com.au
Can design include a lined section for quoting or information? Thanks !

```html
<!DOCTYPE html>
<html lang="en">
<head>
<meta charset="utf-8">
<title>Tidewell Home Care – Business Cards</title>
<link rel="stylesheet" href="https://fonts.googleapis.com/css2?family=Roboto+Condensed:wght@400;700;900&display=swap">
<style>
  :root {
    --stage: #3a3a3a;
    --brand-blue: #0d55a5;
    --brand-red: #e8383b;
    --paper: #ffffff;
    --ink-light: #ffffff;
    --card-w: 520px;
    --card-h: 300px;
    --radius: 22px;
  }
  * { box-sizing: border-box; margin: 0; padding: 0; }
  html, body { width: 1200px; height: 689px; overflow: hidden; }
  body {
    background: var(--stage);
    font-family: "Roboto Condensed", Arial, sans-serif;
    position: relative;
  }
  .card {
    position: absolute;
    top: 195px;
    width: var(--card-w);
    height: var(--card-h);
    border-radius: var(--radius);
    overflow: hidden;
    background: var(--brand-blue);
    box-shadow: 0 18px 40px rgba(0,0,0,.45);
  }
  .card--back { left: 54px; }
  .card--front { left: 626px; }

  .wordmark {
    font-weight: 900;
    letter-spacing: -0.5px;
    line-height: 1;
    white-space: nowrap;
  }
  .card--back .wordmark {
    position: absolute;
    left: 0; right: 0; top: 50%;
    transform: translateY(-50%);
    text-align: center;
    font-size: 52px;
    color: var(--ink-light);
  }

  .front-art { position: absolute; inset: 0; width: 100%; height: 100%; }
  .card--front .wordmark {
    position: absolute;
    left: 44px; top: 56px;
    font-size: 42px;
    color: var(--brand-blue);
  }

  .holder {
    position: absolute;
    left: 90px; top: 228px;
    width: 170px;
    text-align: right;
    color: var(--ink-light);
  }
  .holder__name { font-weight: 700; font-size: 20px; letter-spacing: .3px; }
  .holder__role { font-size: 13px; margin-top: 1px; }

  .divider {
    position: absolute;
    left: 274px; top: 214px;
    width: 1px; height: 72px;
    background: rgba(255,255,255,.7);
  }

  .contacts {
    position: absolute;
    left: 288px; top: 214px;
    list-style: none;
    color: var(--ink-light);
    font-size: 13px;
    line-height: 18px;
  }
  .contacts li { display: flex; align-items: center; gap: 6px; white-space: nowrap; }
  .contacts svg { width: 11px; height: 11px; flex: none; fill: var(--ink-light); }
</style>
</head>
<body>

  <section class="card card--back" aria-label="Card back">
    <div class="wordmark">Tidewell Home Care</div>
  </section>

  <section class="card card--front" aria-label="Card front">
    <svg class="front-art" viewBox="0 0 520 300" preserveAspectRatio="none" aria-hidden="true">
      <rect width="520" height="300" fill="var(--brand-blue)"/>
      <path d="M0 0 H520 V44 C430 135 260 190 0 198 Z" fill="var(--brand-red)"/>
      <path d="M0 0 H520 V32 C430 122 260 176 0 184 Z" fill="var(--paper)"/>
    </svg>

    <div class="wordmark">Tidewell Home Care</div>

    <div class="holder">
      <div class="holder__name">DANIEL HARPER</div>
      <div class="holder__role">President</div>
    </div>

    <div class="divider"></div>

    <ul class="contacts">
      <li>
        <svg viewBox="0 0 24 24"><path d="M6.6 10.8a15 15 0 006.6 6.6l2.2-2.2a1 1 0 011-.25 11.4 11.4 0 003.6.57 1 1 0 011 1V20a1 1 0 01-1 1A17 17 0 013 4a1 1 0 011-1h3.5a1 1 0 011 1c0 1.25.2 2.45.57 3.57a1 1 0 01-.25 1z"/></svg>
        07 5123 4800
      </li>
      <li>
        <svg viewBox="0 0 24 24"><path d="M7 1h10a2 2 0 012 2v18a2 2 0 01-2 2H7a2 2 0 01-2-2V3a2 2 0 012-2zm0 3v14h10V4zm5 15.5a1 1 0 100 2 1 1 0 000-2z"/></svg>
        0412 555 019
      </li>
      <li>
        <svg viewBox="0 0 24 24"><path d="M2 5h20v14H2zm2 2v.5l8 5 8-5V7zm0 2.8V17h16V9.8l-8 5z"/></svg>
        admin@tidewellhomecare.com.au
      </li>
      <li>
        <svg viewBox="0 0 24 24"><path d="M12 2a10 10 0 100 20 10 10 0 000-20zm6.9 6h-2.9a15 15 0 00-1.4-3.6A8 8 0 0118.9 8zM12 4c.8 1.2 1.5 2.5 1.9 4h-3.8c.4-1.5 1.1-2.8 1.900-4zM4.3 14a8 8 0 010-4h3.4a16 16 0 000 4zm.8 2h2.9a15 15 0 001.4 3.6A8 8 0 015.1 16zM8 8H5.1a8 8 0 014.3-3.6A15 15 0 008 8zm4 12c-.8-1.2-1.5-2.5-1.9-4h3.8c-.4 1.5-1.1 2.8-1.9 4zm2.3-6H9.7a14 14 0 010-4h4.6a14 14 0 010 4zm.3 5.6A15 15 0 0016 16h2.9a8 8 0 01-4.3 3.6zM16.3 14a16 16 0 000-4h3.4a8 8 0 010 4z"/></svg>
        www.tidewellhomecare.com.au
      </li>
    </ul>
  </section>

</body>
</html>
```